Business card design

I need my logo on this card, things I need the card to have on it
licensed and insured.
owner operators Derek & Milton Halvorsen
my phone number 5418237906
Disaster Recovery, Storm Damage Restoration, Proactive Disaster Plan Management, Roof Repair/Restoration Structural Repair and Reconstruction, Emergency Boarding and Tarping Service, Perimeter Fencing, Emergency Tree Removal,

```html
<!DOCTYPE html>
<html lang="en">
<head>
<meta charset="utf-8">
<title>Halvorsen's Construction – Business Card</title>
<link href="https://fonts.googleapis.com/css2?family=Montserrat:wght@500;600;700&family=Open+Sans:wght@400;600&display=swap" rel="stylesheet">
<style>
  :root {
    --bg: #ededed;
    --card: #ffffff;
    --blue: #3b8ed6;
    --grey: #6b6d70;
    --ink: #3f4145;
    --rule: #9fc6ea;
  }
  * { box-sizing: border-box; margin: 0; padding: 0; }
  html, body { width: 900px; height: 1200px; overflow: hidden; background: var(--bg); }
  body { position: relative; font-family: "Open Sans", Arial, sans-serif; color: var(--ink); }

  .card {
    position: absolute; left: 110px; width: 680px; height: 400px;
    background: var(--card);
  }
  .card--services { top: 285px; }
  .card--contact { top: 745px; }

  .brand {
    position: absolute; left: 40px; width: 250px; text-align: center;
    font-family: "Montserrat", Arial, sans-serif; font-weight: 700;
    color: var(--blue); letter-spacing: 1px;
  }
  .card--services .brand { top: 140px; }
  .card--contact .brand { top: 110px; }
  .brand__mark {
    display: block; width: 46px; height: 46px; margin: 0 auto 16px;
    background: var(--blue);
  }
  .brand__name { display: block; font-size: 25px; line-height: 1.15; }
  .brand__suffix { display: block; font-size: 25px; line-height: 1.15; }

  .services { position: absolute; left: 345px; top: 70px; width: 310px; }
  .services__title {
    font-family: "Montserrat", Arial, sans-serif; font-weight: 700;
    font-size: 16px; color: var(--blue); letter-spacing: .5px; margin-bottom: 14px;
  }
  .services__list { list-style: none; }
  .services__item {
    display: flex; align-items: flex-start; gap: 10px;
    font-size: 13px; line-height: 1.35; color: var(--ink); margin-bottom: 9px;
  }
  .services__item svg { flex: none; width: 13px; height: 13px; margin-top: 2px; }

  .divider {
    position: absolute; left: 318px; top: 62px; width: 2px; height: 200px; background: var(--blue);
  }
  .contact { position: absolute; left: 342px; top: 62px; width: 320px; }
  .contact__name {
    font-family: "Montserrat", Arial, sans-serif; font-weight: 600;
    font-size: 19px; color: var(--blue);
  }
  .contact__role { font-size: 13px; color: var(--grey); margin: 2px 0 14px; }
  .contact__address { font-size: 13px; line-height: 1.45; color: var(--ink); margin-bottom: 10px; }
  .contact__line {
    display: flex; align-items: center; gap: 9px;
    font-size: 13px; line-height: 1.55; color: var(--ink);
  }
  .contact__line svg { width: 13px; height: 13px; flex: none; }

  .credential {
    position: absolute; left: 30px; right: 30px; bottom: 52px;
    display: flex; align-items: center; gap: 16px;
    font-family: "Montserrat", Arial, sans-serif; font-weight: 600;
    font-size: 15px; letter-spacing: 1.5px; color: var(--ink); white-space: nowrap;
  }
  .credential::before, .credential::after {
    content: ""; flex: 1; height: 2px; background: var(--blue);
  }
</style>
</head>
<body>

<section class="card card--services">
  <div class="brand">
    <span class="brand__mark"></span>
    <span class="brand__name">HALVORSEN'S</span>
    <span class="brand__suffix">CONSTRUCTION L.L.C.</span>
  </div>

  <div class="services">
    <h2 class="services__title">OUR SERVICES:</h2>
    <ul class="services__list">
      <li class="services__item"><svg viewBox="0 0 14 14"><rect x="1" y="1" width="12" height="12" rx="2" fill="#3b8ed6"/><path d="M4 7.2l2 2 4-4.4" stroke="#fff" stroke-width="1.6" fill="none"/></svg>Disaster Recovery</li>
      <li class="services__item"><svg viewBox="0 0 14 14"><rect x="1" y="1" width="12" height="12" rx="2" fill="#3b8ed6"/><path d="M4 7.2l2 2 4-4.4" stroke="#fff" stroke-width="1.6" fill="none"/></svg>Storm Damage Restoration</li>
      <li class="services__item"><svg viewBox="0 0 14 14"><rect x="1" y="1" width="12" height="12" rx="2" fill="#3b8ed6"/><path d="M4 7.2l2 2 4-4.4" stroke="#fff" stroke-width="1.6" fill="none"/></svg>Proactive Disaster Plan Management</li>
      <li class="services__item"><svg viewBox="0 0 14 14"><rect x="1" y="1" width="12" height="12" rx="2" fill="#3b8ed6"/><path d="M4 7.2l2 2 4-4.4" stroke="#fff" stroke-width="1.6" fill="none"/></svg>Roof Repair/Restoration Structural<br>Repair and Reconstruction</li>
      <li class="services__item"><svg viewBox="0 0 14 14"><rect x="1" y="1" width="12" height="12" rx="2" fill="#3b8ed6"/><path d="M4 7.2l2 2 4-4.4" stroke="#fff" stroke-width="1.6" fill="none"/></svg>Emergency Boarding and<br>Tarping Service</li>
      <li class="services__item"><svg viewBox="0 0 14 14"><rect x="1" y="1" width="12" height="12" rx="2" fill="#3b8ed6"/><path d="M4 7.2l2 2 4-4.4" stroke="#fff" stroke-width="1.6" fill="none"/></svg>Perimeter Fencing</li>
      <li class="services__item"><svg viewBox="0 0 14 14"><rect x="1" y="1" width="12" height="12" rx="2" fill="#3b8ed6"/><path d="M4 7.2l2 2 4-4.4" stroke="#fff" stroke-width="1.6" fill="none"/></svg>Emergency Tree Removal</li>
    </ul>
  </div>
</section>

<section class="card card--contact">
  <div class="brand">
    <span class="brand__mark"></span>
    <span class="brand__name">HALVORSEN'S</span>
    <span class="brand__suffix">CONSTRUCTION L.L.C.</span>
  </div>

  <div class="divider"></div>

  <div class="contact">
    <h2 class="contact__name">Derek &amp; Milton Halvorsen</h2>
    <p class="contact__role">Owner Operator</p>
    <p class="contact__address">427 Maple Ridge Rd.<br>Greenville, SC 29607</p>
    <p class="contact__line"><svg viewBox="0 0 14 14"><rect width="14" height="14" rx="2" fill="#3b8ed6"/><path d="M4.3 3.2l1.6 0 .7 2-1 .8c.5 1.1 1.3 1.9 2.4 2.4l.8-1 2 .7v1.6c0 .5-.4.9-.9.9C6.6 10.6 3.4 7.4 3.4 4.1c0-.5.4-.9.9-.9z" fill="#fff"/></svg>5418237906</p>
    <p class="contact__line"><svg viewBox="0 0 14 14"><rect width="14" height="14" rx="2" fill="#3b8ed6"/><rect x="3" y="4.2" width="8" height="5.6" fill="none" stroke="#fff" stroke-width="1"/><path d="M3 4.4l4 3 4-3" fill="none" stroke="#fff" stroke-width="1"/></svg>info@halvorsenconstructionllc.com</p>
    <p class="contact__line"><svg viewBox="0 0 14 14"><rect width="14" height="14" rx="2" fill="#3b8ed6"/><circle cx="7" cy="7" r="3.8" fill="none" stroke="#fff" stroke-width="1"/><path d="M3.2 7h7.6M7 3.2c-1.6 2.2-1.6 5.4 0 7.6M7 3.2c1.6 2.2 1.6 5.4 0 7.6" fill="none" stroke="#fff" stroke-width=".9"/></svg>halvorsenconstructionllc.com</p>
  </div>

  <p class="credential">LICENSED AND INSURED</p>
</section>

</body>
</html>
```